GP Information brochure

we are looking for a designed brochure to send to doctors regarding our products and services. i have attached a very brief design and some information to start the design process.
I have also attached a previous flyer so that the theme and designs stay the same
please let me know if you require anything further
our slogan is: "Improving the quality of life for every individual"
Size: A4
Target Market(s)
general practitioners and allied health industry
Industry/Entity Type
Health And Wellness
Look and feel

```html
<!DOCTYPE html>
<html lang="en">
<head>
<meta charset="utf-8">
<title>Movera Health Club – GP Information Brochure</title>
<link rel="stylesheet" href="https://fonts.googleapis.com/css2?family=Montserrat:wght@400;500;600;700&display=swap">
<style>
  :root {
    --backdrop: #3a3b3d;
    --page-grey: #eceef2;
    --ink: #2b3a55;
    --body-ink: #4a5163;
    --brand-blue: #2f55a4;
    --brand-green: #6aae34;
    --brand-orange: #e59a1c;
    --white: #ffffff;
  }
  * { box-sizing: border-box; margin: 0; padding: 0; }
  html, body { width: 1200px; height: 789px; overflow: hidden; }
  body {
    background: var(--backdrop);
    font-family: "Montserrat", sans-serif;
    color: var(--ink);
  }
  .spread {
    position: absolute;
    left: 105px; top: 44px;
    width: 990px; height: 700px;
    display: flex;
    box-shadow: 0 12px 30px rgba(0,0,0,.45);
  }
  .page { position: relative; width: 495px; height: 700px; overflow: hidden; }

  /* ---------- back page ---------- */
  .page--back {
    background: linear-gradient(135deg, #f6f7f9 0%, var(--page-grey) 55%, #dfe2e8 100%);
  }
  .page--back .facets { position: absolute; inset: 0; }
  .about { position: absolute; left: 34px; top: 46px; width: 330px; }
  .about__title {
    font-size: 17px; font-weight: 600; color: var(--ink);
    padding-bottom: 6px; margin-bottom: 10px;
    border-bottom: 2px solid var(--brand-green); display: inline-block;
  }
  .about__text { font-size: 7.4px; line-height: 1.5; color: var(--body-ink); margin-bottom: 8px; }
  .about__quote {
    font-size: 13px; font-weight: 700; color: var(--brand-orange);
    margin-top: 14px; line-height: 1.3;
  }
  .back-photo {
    position: absolute; right: 0; top: 232px; width: 240px; height: 380px;
    background: radial-gradient(ellipse at 50% 35%, #e8c592 0%, #e0b04a 38%, #d9dce2 72%);
  }
  .brand { display: flex; align-items: center; gap: 8px; }
  .brand__mark { width: 26px; height: 26px; border-radius: 50%; background: var(--brand-blue); }
  .brand__name { font-size: 26px; font-weight: 600; color: var(--brand-blue); letter-spacing: 1px; line-height: 1; }
  .brand__sub { font-size: 7px; font-weight: 600; color: var(--brand-green); letter-spacing: 1px; margin-top: 2px; }
  .page--back .brand { position: absolute; left: 34px; top: 382px; }
  .contact { position: absolute; left: 34px; top: 448px; width: 230px; }
  .contact__title {
    font-size: 14px; font-weight: 600; color: var(--ink);
    padding-bottom: 5px; margin-bottom: 10px;
    border-bottom: 2px solid var(--brand-green); display: inline-block;
  }
  .contact__row { display: flex; gap: 8px; font-size: 10px; line-height: 1.35; color: var(--ink); margin-bottom: 6px; }
  .contact__row svg { flex: none; margin-top: 2px; }
  .social { display: flex; gap: 6px; margin-top: 8px; }
  .social__dot { width: 19px; height: 19px; border-radius: 50%; }
  .social__dot--a { background: #3b5a9a; }
  .social__dot--b { background: #3aa7e0; }
  .social__dot--c { background: #1f73b3; }
  .social__dot--d { background: #c8232c; }
  .waves { position: absolute; left: 0; bottom: 0; width: 495px; }
  .site {
    position: absolute; font-size: 12px; color: var(--white);
    display: flex; align-items: center; gap: 6px;
  }
  .site b { font-weight: 700; }
  .page--back .site { left: 34px; bottom: 26px; }

  /* ---------- cover ---------- */
  .page--cover { background: #f1f1f3; }
  .cover-photo {
    position: absolute; left: 0; top: 60px; width: 495px; height: 560px;
    background: linear-gradient(160deg, #f3ede6 0%, #e7cbb5 35%, #c9b4d8 62%, #e8e6ea 100%);
  }
  .cover-top { position: absolute; left: 0; top: 0; width: 495px; }
  .page--cover .brand { position: absolute; right: 38px; top: 88px; }
  .slogan-disc {
    position: absolute; left: 300px; top: 150px;
    width: 200px; height: 200px; border-radius: 50%;
    background: var(--brand-orange);
    display: flex; flex-direction: column; justify-content: center;
    padding-left: 28px;
    font-size: 17px; line-height: 1.15; color: var(--ink);
  }
  .slogan-disc b { font-weight: 700; }
  .page--cover .site { right: 32px; bottom: 92px; }
</style>
</head>
<body>
  <main class="spread">
    <!-- Back page -->
    <section class="page page--back">
      <svg class="facets" width="495" height="700" aria-hidden="true">
        <polygon points="0,0 220,0 90,180" fill="#ffffff" opacity=".45"/>
        <polygon points="220,0 495,0 380,140" fill="#dde1e8" opacity=".6"/>
        <polygon points="90,180 380,140 250,330" fill="#ffffff" opacity=".35"/>
        <polygon points="0,300 250,330 0,520" fill="#e2e5eb" opacity=".5"/>
      </svg>

      <div class="about">
        <h2 class="about__title">About Us</h2>
        <p class="about__text">We understand everyone has different requirements to improve their quality of life. This is the sole reason Movera Health Club has developed into a friendly yet professional environment with flexible options, including online exercise programming. We have a wide range of health providers along with a 24/7 gymnasium for you to improve your health and wellbeing.</p>
        <p class="about__text">Movera is a highly regarded health club organisation based in Southern Sydney that was established in 2005. Movera is owned and operated by Ellis Marlow, a well known accredited exercise physiologist with over 15 years experience in the industry and a back ground in professional sport. Ellis is supported by a range of staff members with a wide span of knowledge, education and experiences who share the Movera vision of</p>
        <p class="about__quote">“Empowering and Improving your quality of life”</p>
      </div>

      <div class="back-photo" role="img" aria-label="Photo of a smiling woman in a yellow top lifting a dumbbell"></div>

      <div class="brand">
        <span class="brand__mark"></span>
        <div>
          <div class="brand__name">movera</div>
          <div class="brand__sub">HEALTH CLUB</div>
        </div>
      </div>

      <div class="contact">
        <h3 class="contact__title">Get In Touch With Us</h3>
        <div class="contact__row">
          <svg width="9" height="11" viewBox="0 0 9 11"><path d="M4.5 0a4 4 0 0 1 4 4c0 3-4 7-4 7s-4-4-4-7a4 4 0 0 1 4-4z" fill="var(--brand-orange)"/><circle cx="4.5" cy="4" r="1.5" fill="#fff"/></svg>
          <span>27 Harbour Vale Road,<br>Kirrawee Sydney NSW 2230</span>
        </div>
        <div class="contact__row">
          <svg width="10" height="10" viewBox="0 0 10 10"><circle cx="5" cy="5" r="4.3" fill="none" stroke="var(--brand-orange)" stroke-width="1.2"/><path d="M3.3 3c.3 1.8 1.5 3.2 3.4 3.8" stroke="var(--brand-orange)" stroke-width="1.2" fill="none"/></svg>
          <span>+612 90001234</span>
        </div>
        <div class="contact__row">
          <svg width="11" height="9" viewBox="0 0 11 9"><rect x=".6" y=".6" width="9.8" height="7.8" fill="none" stroke="var(--brand-orange)" stroke-width="1.2"/><path d="M.6.6l4.9 4 4.9-4" fill="none" stroke="var(--brand-orange)" stroke-width="1.2"/></svg>
          <span>ellis@movera.club</span>
        </div>
        <div class="social">
          <span class="social__dot social__dot--a"></span>
          <span class="social__dot social__dot--b"></span>
          <span class="social__dot social__dot--c"></span>
          <span class="social__dot social__dot--d"></span>
        </div>
      </div>

      <svg class="waves" width="495" height="150" viewBox="0 0 495 150" aria-hidden="true">
        <path d="M0 60 C160 50 330 20 495 0 L495 150 L0 150 Z" fill="var(--brand-blue)"/>
        <path d="M0 70 C160 60 330 30 495 10 L495 150 L0 150 Z" fill="var(--white)"/>
        <path d="M0 76 C160 66 330 36 495 16 L495 150 L0 150 Z" fill="var(--brand-green)"/>
      </svg>
      <div class="site">
        <svg width="11" height="11" viewBox="0 0 11 11"><circle cx="5.5" cy="5.5" r="4.8" fill="none" stroke="#fff"/><path d="M.7 5.5h9.6M5.5.7c2.5 2.6 2.5 7 0 9.6M5.5.7c-2.5 2.6-2.5 7 0 9.6" fill="none" stroke="#fff" stroke-width=".8"/></svg>
        <span>www.<b>movera</b>.club</span>
      </div>
    </section>

    <!-- Cover -->
    <section class="page page--cover">
      <div class="cover-photo" role="img" aria-label="Photo of a smiling young woman exercising with dumbbells in a bright gym"></div>

      <svg class="cover-top" width="495" height="230" viewBox="0 0 495 230" aria-hidden="true">
        <path d="M0 0 H495 V20 C330 40 130 90 0 200 Z" fill="var(--brand-blue)"/>
        <path d="M0 200 C130 90 330 40 495 20 V30 C330 55 140 110 0 225 Z" fill="var(--brand-orange)"/>
        <path d="M0 225 C60 170 110 140 160 120 C110 150 50 200 0 230 Z" fill="var(--brand-green)"/>
      </svg>

      <div class="brand">
        <span class="brand__mark"></span>
        <div>
          <div class="brand__name">movera</div>
          <div class="brand__sub">HEALTH CLUB</div>
        </div>
      </div>

      <div class="slogan-disc">
        <span>We are here</span>
        <span>to <b>improve</b></span>
        <b>your quality</b>
        <b>of life</b>
      </div>

      <svg class="waves" width="495" height="200" viewBox="0 0 495 200" aria-hidden="true">
        <path d="M0 110 C180 110 360 60 495 0 L495 200 L0 200 Z" fill="var(--brand-blue)"/>
        <path d="M0 135 C180 130 360 90 495 40 L495 200 L0 200 Z" fill="var(--white)"/>
        <path d="M0 142 C180 137 360 97 495 48 L495 200 L0 200 Z" fill="var(--brand-green)"/>
      </svg>
      <div class="site">
        <svg width="11" height="11" viewBox="0 0 11 11"><circle cx="5.5" cy="5.5" r="4.8" fill="none" stroke="#fff"/><path d="M.7 5.5h9.6M5.5.7c2.5 2.6 2.5 7 0 9.6M5.5.7c-2.5 2.6-2.5 7 0 9.6" fill="none" stroke="#fff" stroke-width=".8"/></svg>
        <span>www.<b>movera</b>.club</span>
      </div>
    </section>
  </main>
</body>
</html>
```